Create a Creative Shopify banner for a Streetwear Brand

We need a banner for our brand Corven Studios explaining the meaning of our brand we want the banner to be a simple professional looking design of a wizard/sage/magi looking up at the stars looking at a big four pointed star. we want the design to be black and white. and have this text in a aesthetic font underneath it.
"Corven Studios is a spiritually inspired streetwear brand that fuses modern aesthetics with sacred symbols and cosmic motifs. Drawing inspiration from the Magi—wise sages who followed the stars in search of enlightenment—our designs serve as a reminder that the universe is always guiding us."
we want it to match the stars from the ai file of our brand banner I put in the files. I also put a simple drawing I made and some pictures of wizards into the files as a reference. here is our website for reference corven-studios.com

```html
<!DOCTYPE html>
<html lang="en">
<head>
<meta charset="utf-8">
<title>Corven Studios Story Banner</title>
<link rel="stylesheet" href="https://fonts.googleapis.com/css2?family=Fraunces:opsz,wght@9..144,600;9..144,700&display=swap">
<style>
  :root {
    --night: #000000;
    --starlight: #ffffff;
    --glow: rgba(255, 255, 255, 0.85);
    --robe-light: #d9d9d9;
    --robe-dark: #3a3a3a;
    --ground: #f2f2f2;
  }
  * { margin: 0; padding: 0; box-sizing: border-box; }
  html, body {
    width: 1200px;
    height: 426px;
    overflow: hidden;
    background: var(--night);
  }
  .banner {
    position: relative;
    width: 1200px;
    height: 426px;
    background: var(--night);
    color: var(--starlight);
    font-family: "Fraunces", Georgia, serif;
    overflow: hidden;
  }
  .star-field {
    position: absolute;
    inset: 0;
    width: 1200px;
    height: 426px;
  }
  .star-field use { fill: var(--starlight); }
  .guiding-star {
    position: absolute;
    left: 293px;
    top: 47px;
    width: 82px;
    height: 80px;
    background: radial-gradient(circle at 50% 50%, var(--glow) 0%, rgba(255,255,255,0.25) 22%, rgba(255,255,255,0) 60%);
  }
  .headline {
    position: absolute;
    top: 27px;
    left: 0;
    width: 1200px;
    text-align: center;
    font-size: 28px;
    font-weight: 700;
    line-height: 36px;
  }
  .brand-story {
    position: absolute;
    top: 102px;
    left: 320px;
    width: 560px;
    text-align: center;
    font-size: 19px;
    font-weight: 600;
    line-height: 28.1px;
  }
  .ground-illustration {
    position: absolute;
    left: 300px;
    top: 334px;
    width: 870px;
    height: 22px;
    background: linear-gradient(90deg, var(--ground) 0%, var(--starlight) 50%, var(--ground) 100%);
    border-radius: 11px;
  }
  .sage-illustration {
    position: absolute;
    left: 976px;
    top: 95px;
    width: 160px;
    height: 250px;
    background: linear-gradient(180deg, var(--robe-light) 0%, var(--robe-dark) 100%);
    border-radius: 60px 60px 10px 10px;
  }
  .section-label {
    position: absolute;
    right: 40px;
    top: 374px;
    font-size: 17.5px;
    font-weight: 700;
    line-height: 24px;
  }
</style>
</head>
<body>
<main class="banner">
  <svg class="star-field" viewBox="0 0 1200 426" aria-hidden="true">
    <defs>
      <path id="sparkle" d="M0,-8 Q1,-1 8,0 Q1,1 0,8 Q-1,1 -8,0 Q-1,-1 0,-8Z"/>
      <path id="sparkle-small" d="M0,-4 Q0.5,-0.5 4,0 Q0.5,0.5 0,4 Q-0.5,0.5 -4,0 Q-0.5,-0.5 0,-4Z"/>
    </defs>
    <use href="#sparkle" x="31" y="38"/>
    <use href="#sparkle" x="176" y="14"/>
    <use href="#sparkle" x="246" y="42"/>
    <use href="#sparkle" x="114" y="70"/>
    <use href="#sparkle" x="68" y="133"/>
    <use href="#sparkle" x="156" y="172"/>
    <use href="#sparkle" x="270" y="182"/>
    <use href="#sparkle" x="42" y="226"/>
    <use href="#sparkle" x="117" y="250"/>
    <use href="#sparkle" x="239" y="251"/>
    <use href="#sparkle" x="42" y="314"/>
    <use href="#sparkle" x="276" y="315"/>
    <use href="#sparkle" x="171" y="332"/>
    <use href="#sparkle" x="98" y="376"/>
    <use href="#sparkle" x="216" y="386"/>
    <use href="#sparkle" x="350" y="14"/>
    <use href="#sparkle" x="448" y="90"/>
    <use href="#sparkle" x="528" y="88"/>
    <use href="#sparkle" x="573" y="14"/>
    <use href="#sparkle" x="618" y="73"/>
    <use href="#sparkle" x="668" y="92"/>
    <use href="#sparkle" x="726" y="86"/>
    <use href="#sparkle" x="859" y="12"/>
    <use href="#sparkle" x="861" y="80"/>
    <use href="#sparkle" x="935" y="40"/>
    <use href="#sparkle" x="938" y="116"/>
    <use href="#sparkle" x="1039" y="60"/>
    <use href="#sparkle" x="1111" y="80"/>
    <use href="#sparkle" x="1177" y="21"/>
    <use href="#sparkle" x="1150" y="157"/>
    <use href="#sparkle" x="839" y="197"/>
    <use href="#sparkle" x="975" y="217"/>
    <use href="#sparkle" x="902" y="255"/>
    <use href="#sparkle" x="1166" y="273"/>
    <use href="#sparkle" x="864" y="285"/>
    <use href="#sparkle" x="504" y="286"/>
    <use href="#sparkle" x="701" y="296"/>
    <use href="#sparkle" x="428" y="299"/>
    <use href="#sparkle" x="323" y="295"/>
    <use href="#sparkle" x="1153" y="364"/>
    <use href="#sparkle" x="864" y="390"/>
    <use href="#sparkle" x="738" y="404"/>
    <use href="#sparkle" x="580" y="401"/>
    <use href="#sparkle" x="486" y="406"/>
    <use href="#sparkle" x="1075" y="406"/>
    <use href="#sparkle" x="317" y="394"/>
    <use href="#sparkle-small" x="98" y="12"/>
    <use href="#sparkle-small" x="190" y="79"/>
    <use href="#sparkle-small" x="68" y="100"/>
    <use href="#sparkle-small" x="146" y="108"/>
    <use href="#sparkle-small" x="117" y="173"/>
    <use href="#sparkle-small" x="86" y="218"/>
    <use href="#sparkle-small" x="308" y="230"/>
    <use href="#sparkle-small" x="56" y="389"/>
    <use href="#sparkle-small" x="299" y="324"/>
    <use href="#sparkle-small" x="367" y="198"/>
    <use href="#sparkle-small" x="698" y="69"/>
    <use href="#sparkle-small" x="706" y="7"/>
    <use href="#sparkle-small" x="917" y="165"/>
    <use href="#sparkle-small" x="957" y="161"/>
    <use href="#sparkle-small" x="1187" y="80"/>
    <use href="#sparkle-small" x="497" y="383"/>
    <use href="#sparkle-small" x="1020" y="373"/>
  </svg>

  <div class="guiding-star" role="img" aria-label="Large four-pointed guiding star ornament glowing above the text"></div>

  <h1 class="headline">Clothing for the Mystically inclined</h1>

  <p class="brand-story">
    "Corven Studios is a spiritually inspired streetwear<br>
    brand that fuses modern aesthetics with sacred<br>
    symbols and cosmic motifs. Drawing inspiration<br>
    from the Magi—wise sages who followed the<br>
    stars in search of enlightenment—our designs<br>
    serve as a reminder that the universe is always<br>
    guiding us."
  </p>

  <div class="ground-illustration" role="img" aria-label="White hand-drawn rocky ground line stretching across the lower banner"></div>
  <div class="sage-illustration" role="img" aria-label="Black and white illustration of a robed wizard sage with a pointed hat holding a glowing staff, gazing up at the stars"></div>

  <p class="section-label">Corven Studios Story</p>
</main>
</body>
</html>
```